Bridgeway, Lantern, and the Quiet Harbor Loop Research Program Website

Overview: This website will serve a new research program (Bridgeway, Lantern, and the Quiet Harbor Loop) at the Fenmoor University School of Medicine. I want a clean, intuitive design that has a navigation bar, but uses icons/graphic buttons to link to the main pages. In an attached Word document, I have provided a basic information architecture for the site, understanding that this project would just generate graphics and code for the 3 pages. I highlighted the 3 pages I'd like designed.
Target market: People who want to participate in our research, or contribute grant funding to specific projects.
Number of page: The design project focuses on 3 pages, but the site must accommodate 6 pages with top-level links. See attached Word doc.
Logo and website header: Please integrate our logo in the header. I've uploaded it as a png file--both with the name of the website and with just the logo image. I imaging the logo would look great in a banner set against an image of a mountain. The two main design themes I want to see included are nature and healthcare.
Text content: I have not yet provided text. Use some dummy text.
Technical Specifications:
- Build using WordPress. We will host this site ourselves on Brimloft using WordPress.
- The design package must be coded.
- The template must be responsive to different platforms (e.g., computer, mobile phone, iPad).
Thank you! I look forward to seeing your designs.
- Ned

```html
<!DOCTYPE html>
<html lang="en">
<head>
<meta charset="utf-8">
<title>Bridgeway, Lantern, and the Quiet Harbor Loop – The Research Program</title>
<link rel="stylesheet" href="https://fonts.googleapis.com/css2?family=Oswald:wght@300;400;500;600&family=Open+Sans:wght@400;600&family=Great+Vibes&display=swap">
<style>
:root{
  --navy:#1c4f95;
  --blue:#0e64ae;
  --teal:#0aa386;
  --teal-dark:#08846f;
  --green:#7ed321;
  --ink:#555;
  --pale:#f1f1f1;
  --row:#dedede;
  --white:#fff;
}
*{box-sizing:border-box;margin:0;padding:0}
html,body{width:1200px;height:2816px;overflow:hidden}
body{position:relative;font-family:"Open Sans",Arial,sans-serif;background:var(--white);color:var(--ink)}
.abs{position:absolute}

/* hero */
.hero{left:0;top:0;width:1200px;height:600px;background:linear-gradient(180deg,#eef0f2 0%,#dde2e4 28%,#8a9a6a 55%,#4f7a2a 75%,#345a1a 100%)}
.hero-glow{left:820px;top:0;width:380px;height:600px;background:radial-gradient(circle at 80% 40%,rgba(255,250,210,.9),rgba(255,250,210,0) 60%)}
.nav{top:0;left:0;width:1200px;height:141px;border-bottom:1px solid rgba(120,130,150,.45)}
.nav a{position:absolute;top:58px;font-family:"Oswald",sans-serif;font-size:17px;color:var(--navy);text-decoration:none}
.brand{left:544px;top:40px;width:114px;display:flex;flex-direction:column;align-items:center;gap:4px}
.brand-dot{width:36px;height:36px;border-radius:50%;background:var(--teal)}
.brand-name{font-family:"Oswald",sans-serif;font-size:16px;font-weight:500;color:var(--navy)}
.hero-sub{top:240px;left:0;width:1208px;text-align:center;font-family:"Oswald",sans-serif;font-weight:300;font-size:31px;color:var(--navy)}
.hero-title{top:278px;left:0;width:1208px;text-align:center;font-family:"Oswald",sans-serif;font-weight:500;font-size:56px;color:var(--green);letter-spacing:.5px}
.hero-btn{top:384px;width:110px;text-align:center}
.hero-btn .ring{width:106px;height:106px;border-radius:50%;border:2px solid #fff;margin:0 auto;display:flex;align-items:center;justify-content:center}
.hero-btn span{display:block;margin-top:14px;font-family:"Oswald",sans-serif;font-size:16px;color:#fff;white-space:nowrap}

/* people */
.people-block{left:91px;top:847px;width:378px;height:354px;background:linear-gradient(160deg,#0a7a86,#0b5fa8 60%,#0a9a7e)}
.people-frame{left:135px;top:731px;width:410px;height:439px;background:#fff;box-shadow:0 2px 14px rgba(0,0,0,.2);padding:9px}
.people-photo{width:100%;height:100%;background:linear-gradient(135deg,#e8ecef,#5d7fb8 45%,#d9dde0)}
.people-h{left:574px;top:748px;font-family:"Great Vibes",cursive;font-size:64px;color:var(--navy)}
.divider{display:flex;align-items:center;gap:10px}
.divider i{display:block;width:34px;height:1px;background:currentColor}
.divider b{display:block;width:12px;height:12px;border-radius:50%;border:2px solid currentColor}
.people-div{left:590px;top:848px;color:#666}
.people-p{left:575px;top:884px;width:537px;font-size:13px;line-height:28px;text-align:justify}
.feature{top:1034px;width:170px;text-align:center;font-family:"Oswald",sans-serif;font-size:16px;color:#333}
.feature svg{display:block;margin:0 auto 18px}

/* research band */
.band{left:0;top:1330px;width:1200px;height:550px;background:linear-gradient(90deg,#0d4ea3,#0a86a0 55%,#0aa17c)}
.band-h{top:1455px;left:0;width:1226px;text-align:center;font-family:"Oswald",sans-serif;font-weight:300;font-size:48px;color:#fff}
.band-div{left:560px;top:1546px;color:#fff}
.band-p{left:150px;top:1592px;width:914px;text-align:center;font-size:13px;line-height:28px;color:#fff}
.btn{left:540px;top:1728px;width:147px;height:43px;border-radius:22px;background:var(--navy);color:#fff;font-size:13px;display:flex;align-items:center;justify-content:center}

/* faq */
.faq{left:0;top:1880px;width:1200px;height:673px;background:var(--pale)}
.faq-art{left:70px;top:2070px;width:370px;height:290px;border-radius:6px;background:linear-gradient(135deg,#e9f5d8,#d6e8f4)}
.acc{left:490px;width:647px;height:58px;background:var(--row);display:flex;align-items:center;justify-content:space-between;padding:0 18px 0 18px;font-size:14.5px;color:var(--blue)}
.acc em{font-style:normal;font-size:20px;color:var(--blue)}
.acc-open{color:var(--blue)}
.acc-open strong{color:#333;font-weight:400;margin-right:3px}
.acc-body{left:502px;top:2110px;width:632px;font-size:14.5px;line-height:28px;color:var(--blue)}

/* footer */
.footer{left:0;top:2553px;width:1200px;height:199px;background:var(--blue)}
.foot-h{font-family:"Oswald",sans-serif;font-weight:300;font-size:24px;color:#fff}
.foot-h b{font-weight:500}
.email{left:56px;top:2659px;width:251px;height:36px;background:#fff;border-radius:2px;font-size:13px;color:#777;padding:9px 14px}
.sub{left:311px;top:2658px;width:103px;height:37px;background:var(--teal);color:#fff;font-family:"Oswald",sans-serif;font-size:16px;display:flex;align-items:center;justify-content:center}
.foot-brand{left:556px;top:2615px;width:130px;display:flex;flex-direction:column;align-items:center;gap:8px}
.foot-brand .brand-dot{background:#fff;width:44px;height:44px}
.foot-brand .brand-name{color:#fff;font-size:18px}
.social{left:882px;top:2652px;display:flex;gap:10px}
.social span{width:37px;height:37px;border-radius:50%;background:#fff;color:var(--blue);font-size:8.5px;font-weight:600;display:flex;align-items:center;justify-content:center}
.bar{left:0;top:2752px;width:1200px;height:64px;background:var(--teal);color:#fff;font-size:13px}
.crumbs{left:50px;top:2774px;color:#fff;font-size:13px;word-spacing:2px}
.crumbs span{margin:0 12px}
.copy{left:886px;top:2776px;color:#fff;font-size:13px}
</style>
</head>
<body>

<section class="abs hero" role="img" aria-label="Photograph of a caregiver walking with an elderly person across a sunlit green field"></section>
<div class="abs hero-glow"></div>

<header class="abs nav">
  <a style="left:268px">Home</a>
  <a style="left:355px">People</a>
  <a style="left:452px">Projects</a>
  <div class="abs brand"><i class="brand-dot"></i><span class="brand-name">Bridgeway</span></div>
  <a style="left:706px">FAQ's</a>
  <a style="left:791px">Resources</a>
  <a style="left:906px">Contact</a>
</header>

<p class="abs hero-sub">Bridgeway, Lantern, and the Quiet Harbor Loop</p>
<h1 class="abs hero-title">THE RESEARCH PROGRAM</h1>

<div class="abs hero-btn" style="left:283px">
  <div class="ring"><svg width="50" height="50" viewBox="0 0 50 50" fill="none" stroke="#fff" stroke-width="2"><circle cx="17" cy="12" r="6"/><circle cx="33" cy="12" r="6"/><path d="M6 40v-12a8 8 0 0 1 16 0M28 28a8 8 0 0 1 16 0v12M14 44h22"/></svg></div>
  <span>PEOPLE</span>
</div>
<div class="abs hero-btn" style="left:541px">
  <div class="ring"><svg width="54" height="50" viewBox="0 0 54 50" fill="none" stroke="#fff" stroke-width="2"><path d="M4 12l20 4v26L4 38zM44 12l-20 4"/><circle cx="36" cy="26" r="9"/><path d="M43 33l7 7"/></svg></div>
  <span>RESEARCH PROJECTS</span>
</div>
<div class="abs hero-btn" style="left:808px">
  <div class="ring"><svg width="54" height="50" viewBox="0 0 54 50" fill="none" stroke="#fff" stroke-width="2"><circle cx="20" cy="24" r="15"/><path d="M12 37l-4 8 10-5"/><path d="M32 12a14 14 0 0 1 16 20l2 8-8-4"/><text x="14" y="31" fill="#fff" stroke="none" font-size="20" font-family="Arial">?</text></svg></div>
  <span>FAQ'S</span>
</div>

<svg class="abs" style="left:0;top:570px" width="1200" height="40" viewBox="0 0 1200 40" preserveAspectRatio="none"><path fill="#fff" d="M0 15l40 5 50-8 60 6 70-4 80 7 60-5 90 4 70-6 80 5 60-3 90 6 70-7 80 4 70-3 90 6 60-5 80 4 50-5 50 3V40H0z"/></svg>

<section>
  <div class="abs people-block"></div>
  <div class="abs people-frame"><div class="people-photo" role="img" aria-label="Photograph from above of a researcher typing at a desk covered in charts and monitors"></div></div>
  <h2 class="abs people-h">People</h2>
  <div class="abs divider people-div"><i></i><b></b><i></i></div>
  <p class="abs people-p">Lorem ipsum dolor sit amet, consectetur adipiscing elit. Sed suscipit maximus sapien, ut posuere elit finibus iaculis. Proin elementum magna sit amet risus pulvinar, a efficitur massa fermentum. Praesent ultrices quam in fermentum ultrices. Quisque nibh augue, cursus ac efficitur ut, maximus sit amet orci. Praesent tempus rutrum dignissim...</p>

  <div class="abs feature" style="left:572px">
    <svg width="70" height="70" viewBox="0 0 70 70" fill="none" stroke="#0aa386" stroke-width="2.5"><circle cx="35" cy="34" r="13"/><path d="M26 34h5l3-5 4 9 3-4h4"/><circle cx="35" cy="8" r="4"/><circle cx="10" cy="52" r="4"/><circle cx="60" cy="52" r="4"/><path d="M4 64a6 6 0 0 1 12 0M54 64a6 6 0 0 1 12 0M16 20a28 28 0 0 0-6 22M54 20a28 28 0 0 1 6 22"/></svg>
    Research Team
  </div>
  <div class="abs feature" style="left:756px">
    <svg width="76" height="70" viewBox="0 0 76 70" fill="#0aa386"><ellipse cx="38" cy="34" rx="26" ry="12"/><circle cx="12" cy="18" r="6"/><circle cx="64" cy="18" r="6"/><circle cx="26" cy="10" r="6"/><circle cx="50" cy="10" r="6"/><circle cx="8" cy="44" r="6"/><circle cx="68" cy="44" r="6"/><path d="M22 48h32l-4 12H26z"/></svg>
    Advisory committee
  </div>
  <div class="abs feature" style="left:942px">
    <svg width="76" height="70" viewBox="0 0 76 70" fill="none" stroke="#0aa386" stroke-width="2.5"><path d="M4 22l10-12 10 8-10 12zM72 22L62 10 52 18l10 12zM24 18l12 4 10-6 8 4M14 30l16 18a4 4 0 0 0 6-1l4 3a4 4 0 0 0 6-2l3 2a4 4 0 0 0 6-4L62 30"/><path d="M36 22l-6 8a3 3 0 0 0 5 3l8-6"/></svg>
    Partners
  </div>
</section>

<section>
  <div class="abs band" role="img" aria-label="Photograph of hands reviewing research documents, tinted blue to teal"></div>
  <svg class="abs" style="left:0;top:1325px" width="1200" height="30" viewBox="0 0 1200 30" preserveAspectRatio="none"><path fill="#fff" d="M0 0H1200V8l-60 6-80-5-70 7-90-4-60 5-80-6-70 4-90-3-60 6-80-5-70 3-90-4-60 6-80-4-70 5-60-6-50 4V0z"/></svg>
  <h2 class="abs band-h">Research Projects</h2>
  <div class="abs divider band-div"><i></i><b></b><i></i></div>
  <p class="abs band-p">Aenean efficitur pretium viverra. Aliquam rutrum mauris nunc, et rutrum dolor hendrerit eu. Integer vitae nisi eget enim imperdiet mattis id id sem. Aenean malesuada quis arcu at vulputate. Vivamus tristique, urna aliquam ultricies posuere, est ex aliquet nisl, id malesuada arcu orci vitae sem. Praesent cursus ornare egestas. Donec tempus risus vel est aliquam pharetra.</p>
  <div class="abs btn">Read More</div>
</section>

<section>
  <div class="abs faq"></div>
  <svg class="abs" style="left:0;top:1860px" width="1200" height="30" viewBox="0 0 1200 30" preserveAspectRatio="none"><path fill="#0b6aa6" d="M0 0H1200V14l-70-6-80 7-60-4-90 5-70-6-80 4-60-3-90 6-70-5-80 4-60-6-90 5-70-3-80 6-60-4-50 5-40-4V0z"/><path fill="#f1f1f1" d="M0 30V14l40 4 60-5 80 6 70-4 60 3 90-6 70 5 80-4 60 6 90-5 70 3 80-6 60 4 90-5 70 6 80-4 60 5 40-3V30z"/></svg>
  <div class="abs faq-art" role="img" aria-label="Illustration of the word FAQ surrounded by clouds, speech bubbles and question marks"></div>

  <div class="abs acc acc-open" style="top:2035px"><span><strong>Q1.</strong>What makes this project unique?</span><em>–</em></div>
  <p class="abs acc-body">Aenean efficitur pretium viverra. Aliquam rutrum mauris nunc, et rutrum dolor hendrerit eu. Integer vitae nisi eget enim imperdiet mattis id id sem. Aenean malesuada quis arcu at vulputate.</p>
  <div class="abs acc" style="top:2209px"><span>Q2.&nbsp; Does this project assume that the impact of religion is always positive?</span><em>+</em></div>
  <div class="abs acc" style="top:2286px"><span>Q3.&nbsp; How can I collaborate?</span><em>+</em></div>
  <div class="abs acc" style="top:2364px"><span>Q4.&nbsp; Will Fenmoor faculty lead all projects?</span><em>+</em></div>
</section>

<footer>
  <div class="abs footer"></div>
  <p class="abs foot-h" style="left:56px;top:2600px">Signup <b>Newsletter</b> :</p>
  <div class="abs email">Your Email</div>
  <div class="abs sub">SUBSCRIBE</div>
  <div class="abs foot-brand"><i class="brand-dot"></i><span class="brand-name">Bridgeway</span></div>
  <p class="abs foot-h" style="left:969px;top:2600px">Stay <b>In Touch</b> :</p>
  <div class="abs social"><span>Kin</span><span>Grid</span><span>Chirp</span><span>Well</span><span>Ring</span></div>
  <div class="abs bar"></div>
  <nav class="abs crumbs">Home<span>/</span>People<span>/</span>Research Projects<span>/</span>FAQ's<span>/</span>Resources<span>/</span>Contact</nav>
  <p class="abs copy">Copyright ©&nbsp; 2010-2021&nbsp; All rights reserved</p>
</footer>

</body>
</html>
```